UI Design & Web Design for Used Car Dealer.
Modern and user friendly responsive layout for mobiles and desktop. Bootstrap and form elements for members,registration process,login,dashboard. Layouts for Home Page, Car Listing Pages, Individual Car Information page and etc.

Output files in Bootstrap Html/CSS
Please refer to attachments for more details.

Target Market(s)

Asia / Singapore

Industry/Entity Type

Car Dealer

Coding

Coded - Design and coding required

Number of Pages Required

5+ page

Font styles to use
Sans Serif

Colors
acd037
f6faec
cfcfcf
b1b1b1
ffffff

Requirements
Must have
• Coded in Bootstrap 3 UI Elements, Forms, Labels, Sections, Tables, Buttons, Alerts, Modal, Fonts, Dashboard, Login, Register,Contact
Nice to have
• Stock Images
Should not have
• NA

```html
<!DOCTYPE html>
<html lang="en">
<head>
<meta charset="utf-8">
<title>Drivora – Vehicle Listings</title>
<link rel="stylesheet" href="https://fonts.googleapis.com/css2?family=Michroma&family=Open+Sans:wght@400;600;700&display=swap">
<style>
:root{
  --green:#acd037;
  --green-soft:#f6faec;
  --line:#cfcfcf;
  --muted:#b1b1b1;
  --white:#ffffff;
  --page:#f4f5f7;
  --ink:#333333;
  --text:#666666;
  --dark:#262626;
}
*{box-sizing:border-box;margin:0;padding:0}
html,body{width:1200px;height:2387px;overflow:hidden}
body{background:var(--page);font-family:"Open Sans",Arial,sans-serif;color:var(--ink);position:relative}

.site-header{position:absolute;top:0;left:0;width:1200px;height:98px;background:var(--white);border-top:4px solid var(--green);border-bottom:2px solid #e2e4e8}
.brand{position:absolute;left:84px;top:22px;display:flex;align-items:center;gap:14px}
.brand-mark{width:54px;height:44px;background:var(--green);border-radius:4px}
.brand-name{font-family:"Michroma",sans-serif;font-size:25px;color:var(--green);letter-spacing:1px}
.main-nav{position:absolute;top:0;right:84px;height:92px;display:flex;gap:48px;align-items:center}
.main-nav a{font-size:12.5px;font-weight:700;color:#444;text-decoration:none;letter-spacing:.5px;position:relative;height:92px;display:flex;align-items:center}
.main-nav a.is-active::after{content:"";position:absolute;left:-8px;right:-8px;bottom:-2px;height:4px;background:var(--green)}

.page-title{position:absolute;top:128px;width:1200px;text-align:center;font-family:"Michroma",sans-serif;font-size:30px;color:#3a3a3a;letter-spacing:1px}
.page-title span{color:var(--green)}
.page-subtitle{position:absolute;top:178px;width:1200px;text-align:center;font-size:16px;font-weight:700;color:#444;letter-spacing:1px}

.feature-row{position:absolute;top:231px;left:84px;display:flex;gap:4px}
.feature{position:relative;width:341px;height:302px}
.feature-photo{position:absolute;inset:0}
.feature-caption{position:absolute;left:0;right:0;bottom:0;height:71px;background:rgba(0,0,0,.55);color:#fff;font-size:14px;font-weight:700;text-align:center;line-height:25px;padding-top:11px}

.filter-band{position:absolute;top:578px;left:0;width:1200px;height:92px;background:var(--green)}
.filter{position:absolute;top:24px;width:185px;height:44px;background:#fff;border-radius:3px;box-shadow:0 1px 3px rgba(0,0,0,.15);font-size:12px;color:#777;padding:14px 0 0 14px}
.filter::before{content:"";position:absolute;right:38px;top:13px;width:1px;height:18px;background:var(--line)}
.filter::after{content:"";position:absolute;right:14px;top:20px;border:5px solid transparent;border-top-color:#666}

.sidebar{position:absolute;top:710px;left:84px;width:273px}
.sidebar-head{display:flex;justify-content:space-between;align-items:center;font-size:14px;font-weight:700;color:#333;letter-spacing:.5px;padding-bottom:6px;position:relative}
.sidebar-head::after{content:"";position:absolute;left:0;bottom:-3px;width:46px;height:3px;background:var(--green)}
.category-list{list-style:none;margin-top:14px}
.category-list li{height:27px;border-bottom:1px solid #e3e3e3;font-size:11px;color:#777;display:flex;align-items:center;padding-left:10px;gap:14px}
.category-list li::before{content:"»";color:#888;font-size:12px}

.listing{position:absolute;left:377px;width:737px;height:226px;background:#fff;border:1px solid #e3e5e8;border-radius:5px}
.listing-photo{position:absolute;left:13px;top:13px;width:233px;height:197px;border-radius:5px;overflow:hidden}
.sold-tag{position:absolute;left:-26px;top:14px;width:104px;height:22px;background:var(--green);color:#fff;font-size:12px;font-weight:700;text-align:center;line-height:22px;transform:rotate(-45deg)}
.listing-date{position:absolute;left:256px;top:20px;width:48px;text-align:center;font-family:"Michroma",sans-serif;line-height:1.2}
.listing-date .day{display:block;font-size:19px;color:var(--green)}
.listing-date .month{display:block;font-size:11px;color:#333}
.listing-date .year{display:block;font-size:14px;color:#333}
.listing-divider{position:absolute;left:314px;top:18px;width:3px;height:60px;background:var(--green)}
.listing-body{position:absolute;left:332px;top:22px;width:370px}
.listing-title{font-family:"Michroma",sans-serif;font-size:17px;color:#222;font-weight:400}
.listing-spec{margin-top:12px;font-size:15px;font-weight:700;color:var(--green)}
.listing-text{margin-top:12px;width:362px;font-size:12.5px;line-height:23px;color:#666}
.btn-details{display:inline-block;margin-top:14px;border:1px solid var(--line);padding:7px 10px;font-size:10.5px;color:#888;letter-spacing:.3px}

.pagination{position:absolute;top:1958px;left:805px;width:306px;display:flex;justify-content:space-between;font-size:14px;font-weight:700;color:#222}
.pagination .arrow{color:#888;font-weight:400}
.pagination .is-current{color:#e23a3a;position:relative}
.pagination .is-current::after{content:"";position:absolute;left:50%;top:22px;margin-left:-5px;border:5px solid transparent;border-bottom-color:#222}
.pagination-rule{position:absolute;top:1986px;left:830px;width:280px;height:2px;background:linear-gradient(90deg,transparent,#444 30%,#444 70%,transparent)}

.partner-band{position:absolute;top:2039px;left:0;width:1200px;height:116px;background:var(--green);display:flex;gap:33px;padding:22px 0 0 84px}
.partner{width:144px;height:75px;border:1px solid rgba(255,255,255,.45)}

.site-footer{position:absolute;top:2155px;left:0;width:1200px;height:232px;background:var(--dark);color:#ddd}
.social{position:absolute;top:29px;left:391px;display:flex;gap:13px}
.social span{width:59px;height:59px;border:1px solid #ddd;border-radius:50%;display:flex;align-items:center;justify-content:center}
.footer-nav{position:absolute;top:129px;width:1200px;text-align:center;font-size:11.5px;letter-spacing:.5px;color:#eee}
.footer-nav .sep{margin:0 14px}
.copyright{position:absolute;top:170px;width:1200px;text-align:center;font-size:11.5px;color:#ccc}
</style>
</head>
<body>

<header class="site-header">
  <div class="brand"><span class="brand-mark"></span><span class="brand-name">DRIVORA</span></div>
  <nav class="main-nav">
    <a href="#">HOME</a>
    <a href="#">BENEFITS</a>
    <a href="#" class="is-active">VEHICLE LISTINGS</a>
    <a href="#">START ADVERTISING NOW</a>
    <a href="#">CONTACT</a>
  </nav>
</header>

<h1 class="page-title">VEHICLE <span>LISTINGS</span></h1>
<p class="page-subtitle">LISTINGS OF ALL LATEST VEHICLES FOR SALE</p>

<section class="feature-row">
  <article class="feature">
    <div class="feature-photo" role="img" aria-label="White sedan driving on a coastal road under a grey sky" style="background:linear-gradient(180deg,#b9bcc0 0%,#8d9196 45%,#4b4e52 100%)"></div>
    <div class="feature-caption">HALVEX &amp; QUORRIN DEMO THE FUTURE<br>OF DIGITAL RETAIL</div>
  </article>
  <article class="feature">
    <div class="feature-photo" role="img" aria-label="Dark car with glowing red tail light speeding along a road" style="background:linear-gradient(180deg,#9a9a9a 0%,#5c5c5c 50%,#2e2e2e 100%)"></div>
    <div class="feature-caption">HALVEX &amp; QUORRIN DEMO THE FUTURE<br>OF DIGITAL RETAIL</div>
  </article>
  <article class="feature">
    <div class="feature-photo" role="img" aria-label="Man standing beside a silver convertible sports car" style="background:linear-gradient(180deg,#d7dde3 0%,#9ea6ad 55%,#5a5f63 100%)"></div>
    <div class="feature-caption">HALVEX &amp; QUORRIN DEMO THE FUTURE<br>OF DIGITAL RETAIL</div>
  </article>
</section>

<section class="filter-band">
  <div class="filter" style="left:94px">Model :</div>
  <div class="filter" style="left:301px">Year :</div>
  <div class="filter" style="left:508px">Price :</div>
  <div class="filter" style="left:715px">Transmission :</div>
  <div class="filter" style="left:921px">Latest :</div>
</section>

<aside class="sidebar">
  <div class="sidebar-head">CATEGORY
    <svg width="14" height="12" viewBox="0 0 14 12" aria-hidden="true"><g fill="#555"><rect x="0" y="0" width="2" height="2"/><rect x="4" y="0" width="10" height="2"/><rect x="0" y="5" width="2" height="2"/><rect x="4" y="5" width="10" height="2"/><rect x="0" y="10" width="2" height="2"/><rect x="4" y="10" width="10" height="2"/></g></svg>
  </div>
  <ul class="category-list">
    <li>HALVEX</li><li>BELLARO</li><li>FENWICK</li><li>MERIDAN</li><li>LANTORRA</li><li>ROWAN CREST</li>
  </ul>
</aside>

<article class="listing" style="top:705px">
  <div class="listing-photo" role="img" aria-label="Silver sedan parked on a road under a cloudy sky" style="background:linear-gradient(180deg,#8a98a6 0%,#b6bec4 45%,#5d6d4a 65%,#7b7b7b 100%)"></div>
  <div class="listing-date"><span class="day">27</span><span class="month">AUG</span><span class="year">2019</span></div>
  <div class="listing-divider"></div>
  <div class="listing-body">
    <h2 class="listing-title">MERIDAN VELA K7</h2>
    <p class="listing-spec">1 OWNER | AUTO TRANSMISSION</p>
    <p class="listing-text">Upgrading to an suv,needs to sell this vehicle off urgent.Agent maintain,low mileage,always park at basement carpark unde the shades.</p>
    <span class="btn-details">VIEW DETAILS</span>
  </div>
</article>

<article class="listing" style="top:949px">
  <div class="listing-photo" role="img" aria-label="White sedan driving on a coastal road" style="background:linear-gradient(180deg,#9ea3a8 0%,#777c80 50%,#3f4245 100%)"><span class="sold-tag">SOLD</span></div>
  <div class="listing-date"><span class="day">27</span><span class="month">AUG</span><span class="year">2019</span></div>
  <div class="listing-divider"></div>
  <div class="listing-body">
    <h2 class="listing-title">MERIDAN VELA K7</h2>
    <p class="listing-spec">1 OWNER | AUTO TRANSMISSION</p>
    <p class="listing-text">Upgrading to an suv,needs to sell this vehicle off urgent.Agent maintain,low mileage,always park at basement carpark unde the shades.</p>
    <span class="btn-details">VIEW DETAILS</span>
  </div>
</article>

<article class="listing" style="top:1193px">
  <div class="listing-photo" role="img" aria-label="Red sports car parked by mountains under a blue sky" style="background:linear-gradient(180deg,#9fbde0 0%,#c7d3dd 40%,#b4464a 60%,#8f8f8f 100%)"></div>
  <div class="listing-date"><span class="day">27</span><span class="month">AUG</span><span class="year">2019</span></div>
  <div class="listing-divider"></div>
  <div class="listing-body">
    <h2 class="listing-title">MERIDAN VELA K7</h2>
    <p class="listing-spec">1 OWNER | AUTO TRANSMISSION</p>
    <p class="listing-text">Upgrading to an suv,needs to sell this vehicle off urgent.Agent maintain,low mileage,always park at basement carpark unde the shades.</p>
    <span class="btn-details">VIEW DETAILS</span>
  </div>
</article>

<article class="listing" style="top:1437px">
  <div class="listing-photo" role="img" aria-label="Black SUV parked in front of autumn trees" style="background:linear-gradient(180deg,#c49a3a 0%,#8a7a3e 40%,#2c2c2e 65%,#7e7a70 100%)"><span class="sold-tag">SOLD</span></div>
  <div class="listing-date"><span class="day">27</span><span class="month">AUG</span><span class="year">2019</span></div>
  <div class="listing-divider"></div>
  <div class="listing-body">
    <h2 class="listing-title">MERIDAN VELA K7</h2>
    <p class="listing-spec">1 OWNER | AUTO TRANSMISSION</p>
    <p class="listing-text">Upgrading to an suv,needs to sell this vehicle off urgent.Agent maintain,low mileage,always park at basement carpark unde the shades.</p>
    <span class="btn-details">VIEW DETAILS</span>
  </div>
</article>

<article class="listing" style="top:1681px">
  <div class="listing-photo" role="img" aria-label="Black SUV on a road beside green fields" style="background:linear-gradient(180deg,#8cc0e6 0%,#c9dfe9 35%,#4f6a3a 55%,#2a2b2d 75%,#6c8f3c 100%)"></div>
  <div class="listing-date"><span class="day">27</span><span class="month">AUG</span><span class="year">2019</span></div>
  <div class="listing-divider"></div>
  <div class="listing-body">
    <h2 class="listing-title">MERIDAN VELA K7</h2>
    <p class="listing-spec">1 OWNER | AUTO TRANSMISSION</p>
    <p class="listing-text">Upgrading to an suv,needs to sell this vehicle off urgent.Agent maintain,low mileage,always park at basement carpark unde the shades.</p>
    <span class="btn-details">VIEW DETAILS</span>
  </div>
</article>

<nav class="pagination">
  <span class="arrow">«</span><span>1</span><span>2</span><span>3</span><span>4</span><span>5</span><span>6</span><span class="is-current">7</span><span>8</span><span>9</span><span class="arrow">»</span>
</nav>
<div class="pagination-rule"></div>

<section class="partner-band" aria-label="Partners">
  <div class="partner"></div><div class="partner"></div><div class="partner"></div>
  <div class="partner"></div><div class="partner"></div><div class="partner"></div>
</section>

<footer class="site-footer">
  <div class="social">
    <span></span><span></span><span></span><span></span><span></span>
    <span><svg width="18" height="14" viewBox="0 0 18 14" aria-label="Email"><rect x="1" y="1" width="16" height="12" fill="none" stroke="#ddd" stroke-width="1.6"/><polyline points="1,1 9,8 17,1" fill="none" stroke="#ddd" stroke-width="1.6"/></svg></span>
  </div>
  <div class="footer-nav">HOME<span class="sep">|</span>BENEFITS<span class="sep">|</span>VEHICLE LISTINGS<span class="sep">|</span>START ADVERTISING NOW<span class="sep">|</span>CONTACT</div>
  <p class="copyright">© Copyrights 2016 Drivora. All Rights Reserved.</p>
</footer>

</body>
</html>
```